Halvorn spray foam and Environmental

I have business cards but need new ones. The ones I have are very bland. Here is. Y company website http://www.halvornsprayfoam.ca

Also I can send you copies of the current cards
I would also need my current logo on the new design as well.. Also spray foam and Environmental

Industry/Entity Type

Business

Logo Text

Halvorn.

```html
<!DOCTYPE html>
<html lang="en">
<head>
<meta charset="utf-8">
<title>Halvorn Spray Foam and Environmental — Business Card</title>
<link href="https://fonts.googleapis.com/css2?family=Lato:wght@400;700;900&display=swap" rel="stylesheet">
<style>
  :root {
    --purple: #6b3a7f;
    --green: #4ccb1c;
    --ink: #1e1e1e;
    --paper: #ffffff;
    --backdrop: #d9d9dc;
  }
  * { box-sizing: border-box; margin: 0; padding: 0; }
  html, body { width: 1200px; height: 1059px; overflow: hidden; }
  body {
    background: var(--backdrop);
    font-family: "Lato", Arial, sans-serif;
    display: flex; flex-direction: column; align-items: center; justify-content: center;
    gap: 40px;
  }
  .card {
    position: relative; width: 820px; height: 468px;
    background: var(--paper); overflow: hidden;
    box-shadow: 0 6px 18px rgba(0,0,0,.18);
  }
  .brand { position: absolute; display: flex; align-items: center; gap: 34px; }
  .brand-mark { width: 150px; height: 100px; border-radius: 14px; background: var(--purple); }
  .brand-name {
    font-weight: 900; color: var(--purple); font-size: 92px; letter-spacing: 8px; line-height: 1;
  }
  /* Front: services */
  .card-front { border-bottom: 12px solid var(--purple); }
  .card-front .brand { left: 70px; top: 40px; }
  .services { position: absolute; left: 0; right: 0; top: 190px; text-align: center; }
  .services h2 { font-weight: 900; font-size: 30px; letter-spacing: 1px; line-height: 1.15; }
  .services .foam { color: var(--purple); }
  .services .enviro { color: var(--green); margin-top: 6px; }
  .services p {
    font-size: 23px; color: var(--ink); text-transform: uppercase; letter-spacing: .5px; line-height: 1.25;
  }
  .dot { color: var(--purple); margin: 0 6px; }
  .enviro-list .dot { color: var(--green); }
  /* Back: contacts */
  .card-back .brand { left: 70px; top: 60px; }
  .panel { position: absolute; color: #fff; padding: 26px 34px; }
  .panel-foam { left: 0; top: 250px; width: 480px; height: 160px; background: var(--purple); }
  .panel-enviro { left: 480px; top: 190px; width: 340px; height: 220px; background: var(--green); padding-top: 30px; }
  .panel h3 { font-weight: 400; font-size: 28px; letter-spacing: 1px; margin-bottom: 8px; }
  .contact { list-style: none; font-size: 19px; line-height: 1.45; }
  .contact li { display: flex; align-items: center; gap: 12px; }
  .contact svg { width: 16px; height: 16px; flex: none; fill: #fff; }
</style>
</head>
<body>

<section class="card card-front" aria-label="Card front: services">
  <div class="brand">
    <span class="brand-mark"></span>
    <span class="brand-name">HALVORN</span>
  </div>
  <div class="services">
    <h2 class="foam">SPRAY FOAM</h2>
    <p>Roofing Foam<span class="dot">•</span>Slabjacking<span class="dot">•</span>2 Pound / Half Pound</p>
    <p>Sound Proofing<span class="dot">•</span>Batt Insulation<span class="dot">•</span>Attic Blow In</p>
    <h2 class="enviro">ENVIRONMANTAL</h2>
    <div class="enviro-list">
      <p>Air Monitoring<span class="dot">•</span>Asbestos Testing<span class="dot">•</span>Asbestos Removal</p>
      <p>Building Demolition<span class="dot">•</span>Lead Testing<span class="dot">•</span>Mould Removal</p>
    </div>
  </div>
</section>

<section class="card card-back" aria-label="Card back: contacts">
  <div class="brand">
    <span class="brand-mark"></span>
    <span class="brand-name">HALVORN</span>
  </div>
  <div class="panel panel-foam">
    <h3>SPRAY FOAM</h3>
    <ul class="contact">
      <li><svg viewBox="0 0 16 16"><path d="M3 1l3 3-1.5 2a8 8 0 0 0 5.5 5.5L12 10l3 3-2 2C6 15 1 10 1 3z"/></svg>604-555-0147</li>
      <li><svg viewBox="0 0 16 16"><path d="M1 3h14v10H1z M1 3l7 6 7-6" stroke="#6b3a7f" stroke-width="1.2"/></svg>halvornfoam@mailbox.ca</li>
      <li><svg viewBox="0 0 16 16"><circle cx="8" cy="8" r="7"/><path d="M1 8h14M8 1v14M3 4h10M3 12h10" stroke="#6b3a7f" stroke-width="1"/></svg>www.halvornfoam.com</li>
    </ul>
  </div>
  <div class="panel panel-enviro">
    <h3>ENVIRONMENTAL</h3>
    <ul class="contact">
      <li><svg viewBox="0 0 16 16"><path d="M3 1l3 3-1.5 2a8 8 0 0 0 5.5 5.5L12 10l3 3-2 2C6 15 1 10 1 3z"/></svg>604-555-0192</li>
      <li><svg viewBox="0 0 16 16"><path d="M1 3h14v10H1z M1 3l7 6 7-6" stroke="#4ccb1c" stroke-width="1.2"/></svg>halvornenviro@mailbox.ca</li>
      <li><svg viewBox="0 0 16 16"><circle cx="8" cy="8" r="7"/><path d="M1 8h14M8 1v14M3 4h10M3 12h10" stroke="#4ccb1c" stroke-width="1"/></svg>www.halvornenviro.com</li>
    </ul>
  </div>
</section>

</body>
</html>
```